Financial Coaching & Personal Development

I’m desiring a classic business card for my financial coaching and personal development business. The colors I have started with are a goldish brown and hunter green. The brownish color represents soil and green represents growth. I don’t want it it to look masculine. I want the brown to be more of a golden color. I want the color combination and overall design to be timeless not trendy. The logo can be changed as long as it represents growth- moving from where you are to where you want to be.

Target Market(s)

Working Adults with median income $65k; small businesses with a minimum of 20 employees

Industry/Entity Type

Consulting

Contact Information for Business Card

Marla Quenby, MBA
Certified Financial Coach

Font styles to use
Serif

Requirements
Must have
• Logo
My name
Business description
Email marla.quenby@thrivelanefundhouse
Phone number 662-555-0187
Nice to have
• Slogan

```html
<!DOCTYPE html>
<html lang="en">
<head>
<meta charset="UTF-8">
<title>Thrivelane Fund House – Business Card</title>
<link href="https://fonts.googleapis.com/css2?family=Gilda+Display&display=swap" rel="stylesheet">
<style>
  :root {
    --gold-brown: #7a6029;
    --gold-brown-back: #786029;
    --hunter-green: #1f8f3f;
    --paper: #ffffff;
    --ink: #2a2218;
    --stage: #858585;
  }
  * { margin: 0; padding: 0; box-sizing: border-box; }
  html, body {
    width: 1200px; height: 600px; overflow: hidden;
    background: var(--stage);
    font-family: "Gilda Display", Georgia, serif;
  }
  .canvas { position: relative; width: 1200px; height: 600px; }

  .card { position: absolute; width: 438px; height: 251px; overflow: hidden; }
  .card--front { left: 140px; top: 176px; background: var(--paper); }
  .card--back { left: 626px; top: 175px; background: var(--gold-brown-back); }

  .brand-mark { position: absolute; width: 38px; height: 38px; }
  .card--front .brand-mark { left: 198px; top: 56px; background: var(--hunter-green); }
  .card--back .brand-mark { left: 198px; top: 66px; background: var(--paper); }

  .brand-name {
    position: absolute; left: 0; width: 100%; text-align: center;
    font-size: 15px; letter-spacing: 1.6px; text-transform: uppercase;
  }
  .card--front .brand-name { top: 122px; color: var(--gold-brown); }
  .card--back .brand-name { top: 125px; color: var(--paper); }

  .brand-tagline { position: absolute; font-size: 9.5px; letter-spacing: 0.2px; white-space: nowrap; }
  .card--front .brand-tagline { left: 147px; top: 143px; color: var(--hunter-green); }
  .card--back .brand-tagline { left: 157px; top: 146px; color: var(--paper); font-size: 8.5px; }

  .person { position: absolute; left: 36px; top: 188px; }
  .person__name { font-size: 17.5px; color: var(--gold-brown); line-height: 1.1; }
  .person__title { font-size: 12px; color: var(--ink); margin-top: 2px; }

  .divider { position: absolute; left: 213px; top: 199px; width: 1px; height: 21px; background: var(--gold-brown); }

  .contact { position: absolute; left: 219px; top: 195px; list-style: none; }
  .contact__item { display: flex; align-items: center; gap: 6px; font-size: 11px; color: var(--ink); line-height: 14px; }
  .contact__icon { width: 7px; height: 7px; flex: none; }

  .footer-band { position: absolute; left: 0; bottom: 0; width: 100%; height: 13px; display: flex; }
  .footer-band__gold { width: 372px; background: var(--gold-brown); }
  .footer-band__mark { width: 22px; background: var(--paper); display: flex; align-items: center; justify-content: center; }
  .footer-band__mark span { width: 9px; height: 9px; background: var(--hunter-green); }
  .footer-band__green { flex: 1; background: var(--hunter-green); }
</style>
</head>
<body>
<main class="canvas">
  <section class="card card--front" aria-label="Business card front">
    <div class="brand-mark"></div>
    <h1 class="brand-name">Thrivelane Fund House</h1>
    <p class="brand-tagline">Financial Education &amp; Personal Development</p>

    <div class="person">
      <p class="person__name">Marla Quenby, MBA</p>
      <p class="person__title">Certified Financial Coach</p>
    </div>

    <div class="divider"></div>

    <ul class="contact">
      <li class="contact__item">
        <svg class="contact__icon" viewBox="0 0 10 10"><path d="M2 1 L4 3 L3 4 Q4.5 6 6 7 L7 6 L9 8 L8 9.3 Q2 8 0.7 2 Z" fill="var(--gold-brown)"/></svg>
        662-555-0187
      </li>
      <li class="contact__item">
        <svg class="contact__icon" viewBox="0 0 10 8"><rect x="0" y="0.5" width="10" height="7" fill="var(--gold-brown)"/><path d="M0 0.8 L5 4.5 L10 0.8" stroke="#fff" stroke-width="0.9" fill="none"/></svg>
        marla.quenby@thrivelanefundhouse
      </li>
    </ul>

    <div class="footer-band">
      <div class="footer-band__gold"></div>
      <div class="footer-band__mark"><span></span></div>
      <div class="footer-band__green"></div>
    </div>
  </section>

  <section class="card card--back" aria-label="Business card back">
    <div class="brand-mark"></div>
    <h2 class="brand-name">Thrivelane Fund House</h2>
    <p class="brand-tagline">Financial Education &amp; Personal Development</p>
  </section>
</main>
</body>
</html>
```